Inspiring Fundraising Foundation Website to Provide Academic Scholarships

Hello, we are launching a foundation to provide academic scholarships to high school students for college. We'd like this to be an informational website with contact information. There will be a total of approximately 5-7 pages in all.
The color scheme will be purple and white, with a girly feel. I 've attached the logo for reference!

Reason: Extending deadline to go over revisions

Target Market(s)

high school students, college students

Industry/Entity Type

Education

Coding

Coded - Design and coding required

Number of Pages Required

5+ page

Font styles to use
Serif
Sans Serif
Script

Colors
6b449b
886aae
b7a5cd
e4daeb
ffffff
fdf9cf
fbf289

Requirements
Must have
• Purple, girly feel, to reflect the logo's style. Should be light-themed
Should not have
• No dark themes (aka heavy on black or dark colors)

```html
<!DOCTYPE html>
<html lang="en">
<head>
<meta charset="utf-8">
<title>Elena Marisol Foundation</title>
<link href="https://fonts.googleapis.com/css2?family=Roboto:wght@300;400;500;700;900&family=Roboto+Condensed:wght@400;700&display=swap" rel="stylesheet">
<style>
:root{
  --purple:#6b449b;
  --purple-mid:#886aae;
  --purple-soft:#b7a5cd;
  --lavender:#e4daeb;
  --white:#ffffff;
  --cream:#fdf9cf;
  --yellow:#fbf289;
  --ink:#333333;
  --muted:#8a8a8a;
  --line:#e2e2e2;
  --page-bg:#e9e9ea;
  --panel:#f2f2f3;
}
*{box-sizing:border-box;margin:0;padding:0}
html,body{width:1200px;height:3044px;overflow:hidden}
body{background:var(--page-bg);font-family:"Roboto",Arial,sans-serif;color:var(--ink)}
.page{position:absolute;left:80px;top:0;width:1040px;height:3044px;background:var(--white)}

/* header */
.brand{position:absolute;left:20px;top:16px;width:140px;display:flex;flex-direction:column;align-items:flex-start;gap:6px}
.brand-dot{width:34px;height:34px;border-radius:50%;background:var(--purple)}
.brand-name{font-family:"Roboto",sans-serif;font-weight:700;font-size:26px;line-height:28px;color:var(--purple)}
.topbar{position:absolute;right:14px;top:40px;display:flex;align-items:center;gap:22px;font-size:13px;color:#555}
.topbar span{display:flex;align-items:center;gap:7px}
.btn-donate-top{background:var(--purple);color:var(--white);padding:7px 14px;font-weight:500;font-size:12px;letter-spacing:.5px}
.mainnav{position:absolute;left:180px;right:0;top:136px;height:46px;background:var(--purple);display:flex;justify-content:space-around;align-items:center}
.mainnav a{color:var(--white);text-decoration:none;font-size:12px;font-weight:500;letter-spacing:.4px;text-transform:uppercase}
.mainnav a.active{background:var(--purple-mid);padding:15px 18px}

/* hero */
.hero{position:absolute;left:0;top:188px;width:1040px;height:472px;background:linear-gradient(135deg,#b85a4d 0%,#d9b59a 30%,#6f8fb8 55%,#c9a774 78%,#8e4a44 100%)}
.hero-caption{position:absolute;left:690px;top:84px;width:312px;height:250px;background:rgba(46,32,60,.82);padding:30px 28px}
.hero-caption h1{color:var(--white);font-family:"Roboto Condensed",sans-serif;font-weight:700;font-size:40px;line-height:46px}
.btn-outline-light{display:inline-block;margin-top:22px;border:2px solid var(--white);color:var(--white);font-size:12px;font-weight:500;padding:8px 16px;letter-spacing:.5px}
.dots{display:flex;gap:8px;margin-top:20px}
.dots i{width:9px;height:9px;border-radius:50%;background:var(--white);opacity:.6}
.dots i:first-child{opacity:1}

/* feature cards */
.features{position:absolute;left:8px;top:680px;width:1024px;display:flex;gap:14px}
.feature{flex:1;height:280px;border:1px solid var(--line);background:var(--white);text-align:center}
.feature-top{height:100px;background:var(--panel);display:flex;flex-direction:column;align-items:center;justify-content:center}
.feature-icon{width:58px;height:58px;border-radius:50%;background:var(--purple);display:flex;align-items:center;justify-content:center}
.feature h3{font-size:20px;font-weight:500;color:var(--ink);margin-top:-8px;background:var(--panel);padding-bottom:14px}
.feature p{font-size:11px;line-height:17px;color:var(--muted);padding:18px 34px 0}
.more{display:inline-flex;align-items:center;gap:6px;font-size:11px;font-weight:700;color:#555;margin-top:14px;letter-spacing:.3px}
.more b{width:14px;height:14px;background:var(--purple);color:var(--white);font-size:9px;display:inline-flex;align-items:center;justify-content:center}

/* welcome */
.welcome{position:absolute;left:0;top:1000px;width:1040px;text-align:center}
.section-title{font-family:"Roboto Condensed",sans-serif;font-weight:700;font-size:30px;color:#3a3a3a;letter-spacing:.3px}
.welcome p{width:900px;margin:22px auto 0;font-size:12px;line-height:20px;color:var(--muted)}
.btn-outline{display:inline-block;margin-top:24px;border:2px solid #555;color:#444;font-size:11px;font-weight:700;padding:7px 16px;letter-spacing:.5px}

/* scholarships */
.scholar-title{position:absolute;left:0;top:1300px;width:1040px;text-align:center}
.scholar-grid{position:absolute;left:18px;top:1380px;width:1004px;display:flex;gap:16px}
.scholar{flex:1;height:325px;background:var(--white);box-shadow:0 1px 5px rgba(0,0,0,.15);text-align:center}
.scholar-photo{height:168px}
.scholar h4{font-size:16px;font-weight:700;color:var(--purple);margin-top:18px}
.scholar p{font-size:11px;line-height:17px;color:var(--muted);padding:10px 22px 0}

/* register */
.register{position:absolute;left:0;top:1730px;width:1040px;height:410px;background:radial-gradient(circle at 50% 30%,#8a67b3 0%,var(--purple) 55%,#5b3787 100%)}
.register h2{position:absolute;left:0;right:0;top:66px;text-align:center;color:var(--white);font-family:"Roboto Condensed",sans-serif;font-size:42px;font-weight:400;letter-spacing:1px}
.field{position:absolute;background:var(--white);font-size:11px;color:#777;padding:8px 12px;height:28px}
.btn-submit{position:absolute;left:540px;top:310px;width:92px;height:26px;background:var(--yellow);color:#444;font-size:11px;font-weight:700;display:flex;align-items:center;justify-content:center;letter-spacing:.5px}

/* news */
.news-head{position:absolute;left:10px;top:2206px;width:1020px;display:flex;justify-content:space-between;align-items:center}
.news-head h2{font-family:"Roboto Condensed",sans-serif;font-size:30px;font-weight:700;color:#3a3a3a}
.arrows{display:flex;gap:10px;font-size:18px;color:#666}
.news{position:absolute;top:2290px;width:500px;height:190px}
.news-photo{position:absolute;left:0;top:0;width:180px;height:180px;border-radius:50%;border:4px solid var(--lavender)}
.news-body{position:absolute;left:232px;top:4px;width:250px}
.news-body h4{font-size:14px;font-weight:500;color:#444}
.date{display:inline-block;background:var(--purple);color:var(--white);font-size:10px;font-weight:700;padding:4px 10px;margin-top:8px}
.news-body p{font-size:11px;line-height:17px;color:var(--muted);margin-top:10px}

/* partners */
.partners{position:absolute;left:10px;top:2565px;width:1020px;display:flex;justify-content:space-between;align-items:center;padding:0 20px}
.partner{height:30px;background:#c9c9cc;border-radius:3px}
.rule{position:absolute;left:0;width:1040px;height:1px;background:var(--line)}

/* footer */
.footer{position:absolute;left:0;top:2670px;width:1040px;height:374px;background:#f6f6f7}
.foot-col{position:absolute;top:36px}
.foot-col h5{font-size:14px;font-weight:700;color:#444;letter-spacing:.4px}
.foot-col p,.foot-col li{font-size:11px;line-height:18px;color:var(--muted)}
.foot-col ul{list-style:none;margin-top:14px}
.foot-input{width:230px;height:30px;background:var(--white);border:1px solid var(--line);font-size:11px;color:#999;padding:8px 10px;margin-top:16px}
.foot-btn{display:inline-block;margin-top:12px;background:var(--purple);color:var(--white);font-size:10px;font-weight:700;padding:7px 14px}
.contact-row{display:flex;gap:10px;align-items:flex-start;margin-top:14px}
.contact-row svg{flex:none;margin-top:2px}
.foot-brand{position:absolute;left:860px;top:44px;width:150px;display:flex;flex-direction:column;align-items:center;gap:8px;text-align:center}
.socials{position:absolute;left:0;right:0;top:300px;display:flex;justify-content:center;gap:8px}
.socials i{width:22px;height:22px;border-radius:50%;background:var(--purple-mid)}
.copyright{position:absolute;left:0;right:0;top:334px;text-align:center;font-size:10px;color:var(--muted)}
</style>
</head>
<body>
<div class="page">

  <header>
    <div class="brand">
      <div class="brand-dot"></div>
      <div class="brand-name">Elena Marisol Foundation</div>
    </div>
    <div class="topbar">
      <span><svg width="12" height="12" viewBox="0 0 24 24"><path fill="#6b449b" d="M6.6 10.8a15 15 0 006.6 6.6l2.2-2.2c.3-.3.7-.4 1-.2 1.1.4 2.3.6 3.6.6.6 0 1 .4 1 1V20c0 .6-.4 1-1 1A17 17 0 013 4c0-.6.4-1 1-1h3.5c.6 0 1 .4 1 1 0 1.3.2 2.5.6 3.6.1.3 0 .7-.2 1z"/></svg>(555) - 203 - 6491</span>
      <span><svg width="13" height="10" viewBox="0 0 26 20"><rect x="1" y="1" width="24" height="18" fill="none" stroke="#6b449b" stroke-width="2"/><path d="M1 1l12 10L25 1" fill="none" stroke="#6b449b" stroke-width="2"/></svg>info@elenamarisolfoundation.org</span>
      <span><svg width="11" height="12" viewBox="0 0 22 24"><circle cx="11" cy="7" r="6" fill="#6b449b"/><path d="M0 24c0-7 5-10 11-10s11 3 11 10z" fill="#6b449b"/></svg>LOGIN</span>
      <span class="btn-donate-top">DONATE</span>
    </div>
    <nav class="mainnav">
      <a class="active">Home</a><a>About Us</a><a>Scholarship Programs</a><a>Become a Member</a><a>Donate</a><a>Events</a><a>Contact Us</a>
    </nav>
  </header>

  <section class="hero" role="img" aria-label="Photo of young students at desks in a bright classroom">
    <div class="hero-caption">
      <h1>Elena Marisol Foundation</h1>
      <span class="btn-outline-light">READ MORE</span>
      <div class="dots"><i></i><i></i><i></i></div>
    </div>
  </section>

  <section class="features">
    <article class="feature">
      <div class="feature-top"><div class="feature-icon"><svg width="28" height="24" viewBox="0 0 28 24"><path d="M14 4C10 1 5 1 1 2v19c4-1 9-1 13 2 4-3 9-3 13-2V2c-4-1-9-1-13 2z" fill="none" stroke="#fff" stroke-width="2"/><path d="M14 4v19" stroke="#fff" stroke-width="2"/></svg></div></div>
      <h3>High School &amp; College</h3>
      <p>We guide students from their first class to graduation day, offering mentors, study help and planning for college.</p>
      <span class="more">READ MORE <b>&#8250;</b></span>
    </article>
    <article class="feature">
      <div class="feature-top"><div class="feature-icon"><svg width="30" height="24" viewBox="0 0 30 24"><path d="M15 2L1 9l14 7 14-7z" fill="#fff"/><path d="M7 13v6c4 3 12 3 16 0v-6l-8 4z" fill="#fff"/><path d="M27 10v8" stroke="#fff" stroke-width="2"/></svg></div></div>
      <h3>Scholarships</h3>
      <p>Each year we award grants to driven students who show promise, heart and a clear plan for their education.</p>
      <span class="more">READ MORE <b>&#8250;</b></span>
    </article>
    <article class="feature">
      <div class="feature-top"><div class="feature-icon"><svg width="22" height="26" viewBox="0 0 22 26"><rect x="1" y="3" width="20" height="22" rx="2" fill="none" stroke="#fff" stroke-width="2"/><rect x="7" y="1" width="8" height="5" fill="#fff"/><path d="M6 13h10M6 18h10" stroke="#fff" stroke-width="2"/></svg></div></div>
      <h3>Donate</h3>
      <p>Your gift helps a student reach college. Every donation goes straight to tuition, books and campus fees.</p>
      <span class="more">READ MORE <b>&#8250;</b></span>
    </article>
  </section>

  <section class="welcome">
    <h2 class="section-title">WELCOME TO ELENA MARISOL FOUNDATION</h2>
    <p>We believe every student deserves the chance to learn, grow and reach for a degree. Our foundation partners with schools, families and local leaders to open doors for young women and men who dream of college. Through scholarships, mentoring and community events, we help students plan their path, apply with confidence and finish strong. Join us as we build a brighter future, one student at a time, and celebrate the hard work of every family we serve.</p>
    <span class="btn-outline">READ MORE</span>
  </section>

  <h2 class="section-title scholar-title">ACADEMIC SCHOLARSHIPS</h2>
  <section class="scholar-grid">
    <article class="scholar"><div class="scholar-photo" role="img" aria-label="Photo of students studying together outdoors" style="background:linear-gradient(135deg,#a9c27a,#d8c6a4,#6e8f4e)"></div><h4>Merit Award Program</h4><p>Support for top students with strong grades and a passion for learning.</p></article>
    <article class="scholar"><div class="scholar-photo" role="img" aria-label="Photo of students sitting on a lawn with books" style="background:linear-gradient(135deg,#7fa35a,#c9d79a,#4f7a3a)"></div><h4>First Generation Grant</h4><p>Help for students who are the first in their family to attend college.</p></article>
    <article class="scholar"><div class="scholar-photo" role="img" aria-label="Photo of graduates in caps and gowns" style="background:linear-gradient(135deg,#3a3a48,#b48a74,#23232c)"></div><h4>Graduate Success Fund</h4><p>Awards that carry students through to their final year and degree.</p></article>
    <article class="scholar"><div class="scholar-photo" role="img" aria-label="Photo of smiling students on a college campus" style="background:linear-gradient(135deg,#c77a5a,#e2c3a2,#5f8a52)"></div><h4>Community Leader Award</h4><p>For students who give back through service and local leadership.</p></article>
  </section>

  <section class="register">
    <h2>REGISTER NOW</h2>
    <div class="field" style="left:168px;top:172px;width:330px">Name</div>
    <div class="field" style="left:168px;top:204px;width:330px">Email</div>
    <div class="field" style="left:168px;top:236px;width:330px">Phone</div>
    <div class="field" style="left:540px;top:172px;width:330px">Subject</div>
    <div class="field" style="left:540px;top:204px;width:330px;height:60px">Message</div>
    <div class="btn-submit">SUBMIT</div>
  </section>

  <div class="news-head"><h2>LATEST NEWS</h2><div class="arrows"><span>&#8249;</span><span>&#8250;</span></div></div>
  <article class="news" style="left:10px">
    <div class="news-photo" role="img" aria-label="Photo of children working in a classroom" style="background:linear-gradient(135deg,#b7a5cd,#d9b39a,#7a8fb0)"></div>
    <div class="news-body"><h4>Spring awards night brings families together</h4><span class="date">FEB 05, 2017</span><p>Our spring gala honored twelve new scholars and their families with a night of music and thanks.</p><span class="more">Read More &#8250;</span></div>
  </article>
  <article class="news" style="left:490px">
    <div class="news-photo" role="img" aria-label="Portrait photo of a scholarship recipient" style="background:linear-gradient(135deg,#e4daeb,#c79a86,#6b449b)"></div>
    <div class="news-body"><h4>New grant opens for fall applicants</h4><span class="date">FEB 05, 2017</span><p>Applications for the fall cycle are now open to all local seniors planning to enroll next year.</p><span class="more">Read More &#8250;</span></div>
  </article>

  <div class="rule" style="top:2530px"></div>
  <div class="partners">
    <div class="partner" style="width:70px"></div>
    <div class="partner" style="width:110px"></div>
    <div class="partner" style="width:110px"></div>
    <div class="partner" style="width:100px"></div>
    <div class="partner" style="width:70px"></div>
    <div class="partner" style="width:90px"></div>
  </div>

  <footer class="footer">
    <div class="foot-col" style="left:20px;width:260px">
      <h5>SIGN UP FOR NEWSLETTER</h5>
      <p style="margin-top:14px">Get foundation news, events and scholarship dates sent to you.</p>
      <div class="foot-input">Enter email</div>
      <span class="foot-btn">SUBMIT</span>
    </div>
    <div class="foot-col" style="left:340px;width:300px">
      <h5>CONTACT US</h5>
      <div class="contact-row"><svg width="10" height="14" viewBox="0 0 20 28"><path d="M10 0a10 10 0 00-10 10c0 8 10 18 10 18s10-10 10-18A10 10 0 0010 0z" fill="#6b449b"/><circle cx="10" cy="10" r="4" fill="#fff"/></svg><p>Elena Marisol Foundation<br>214 Lilac Row, Fairhaven, TX 70000</p></div>
      <div class="contact-row"><svg width="12" height="12" viewBox="0 0 24 24"><path fill="#6b449b" d="M6.6 10.8a15 15 0 006.6 6.6l2.2-2.2c.3-.3.7-.4 1-.2 1.1.4 2.3.6 3.6.6.6 0 1 .4 1 1V20c0 .6-.4 1-1 1A17 17 0 013 4c0-.6.4-1 1-1h3.5c.6 0 1 .4 1 1 0 1.3.2 2.5.6 3.6.1.3 0 .7-.2 1z"/></svg><p>Phone : (555) 203-6491</p></div>
      <div class="contact-row"><svg width="13" height="10" viewBox="0 0 26 20"><rect x="1" y="1" width="24" height="18" fill="none" stroke="#6b449b" stroke-width="2"/><path d="M1 1l12 10L25 1" fill="none" stroke="#6b449b" stroke-width="2"/></svg><p>Email : info@elenamarisolfoundation.org</p></div>
    </div>
    <div class="foot-col" style="left:700px;width:140px">
      <h5>QUICK LINKS</h5>
      <ul><li>Home</li><li>About Us</li><li>Program</li><li>Donate</li><li>Meet the Team</li><li>Contact Us</li></ul>
    </div>
    <div class="foot-brand">
      <div class="brand-dot"></div>
      <div class="brand-name">Elena Marisol Foundation</div>
    </div>
    <div class="socials"><i></i><i></i><i></i><i></i></div>
    <p class="copyright">&copy;2017 Elena Marisol Foundation. All Rights Reserved.</p>
  </footer>

</div>
</body>
</html>
```